Welding and farication business card

Business name Tbm Welding & Fabrication

I need a business card made for my welding and fabrication business that is bold and stands out. My business is both welding repairs on machinery and anything else you can imagine as well as fabricating new products. i have used this service before and was very happy with the out come of my design logo. i think the card should remain fairly simple and classy but also be bold. I think a black card would best be suited to the talk with my logo on it. i feel the back of the card should just have my logo and the front have my logo email, website and phone number and maybe incorporate a facebook and instagram simple if it can be made look good these arnt a necessity.
I have included both my logo and some business card ideas below

Target Market(s)

Farmers, heavy industry, earthmoving, trucking

Industry/Entity Type

Engineering

Contact Information for Business Card

0438517264
dale@tbmweldingandfabrication.com.au
www.tbmweldingandfabrication.com.au

Colors
33a6d7
0255a3

Requirements
Must have
• Dale Hutchins
my phone number 0438517264
my logo
Preferably a black card desgn
Nice to have
• List of what i do,
Sheds and carports
Ute trays
Stockyards
Trailers
Farm equipment
Stockcrates
Gateways and Entrances
Breakdowns
Maintenance
And lots more!

```html
<!DOCTYPE html>
<html lang="en">
<head>
<meta charset="UTF-8">
<title>Tbm Welding &amp; Fabrication – Business Card</title>
<link rel="stylesheet" href="https://fonts.googleapis.com/css2?family=Barlow:ital,wght@0,400;0,600;0,800;1,400;1,800&display=swap">
<style>
  :root {
    --page-bg: #2a2b2e;
    --card-bg: #141415;
    --card-edge: #0255a3;
    --accent: #33a6d7;
    --brand-blue: #1d56a8;
    --text-light: #e4e6ea;
    --text-muted: #b9bcc2;
    --logo-grey: #c9ccd1;
  }
  * { box-sizing: border-box; margin: 0; padding: 0; }
  html, body { width: 1200px; height: 900px; overflow: hidden; }
  body {
    background: var(--page-bg);
    font-family: "Barlow", Arial, sans-serif;
    position: relative;
  }
  .card {
    position: absolute;
    width: 640px;
    height: 390px;
    background: var(--card-bg);
    border-bottom: 9px solid var(--card-edge);
    box-shadow: 0 18px 40px rgba(0,0,0,.55);
    overflow: hidden;
  }
  .card--front { left: 60px; top: 50px; }
  .card--back { left: 500px; top: 460px; }

  /* Front */
  .brand {
    position: absolute;
    display: flex;
    align-items: center;
    gap: 12px;
  }
  .brand__mark {
    width: 16px; height: 16px;
    border-radius: 50%;
    background: var(--accent);
    flex: none;
  }
  .brand__name {
    font-weight: 800;
    color: var(--brand-blue);
    text-transform: uppercase;
    letter-spacing: .5px;
    line-height: 1.05;
  }
  .card--front .brand { left: 40px; top: 44px; }
  .card--front .brand__name { font-size: 30px; }

  .divider {
    position: absolute;
    left: 190px; right: 30px; top: 214px;
    height: 1px;
    background: var(--brand-blue);
  }
  .holder-name {
    position: absolute;
    right: 50px; top: 170px;
    font-size: 30px;
    font-weight: 800;
    font-style: italic;
    color: var(--brand-blue);
    text-transform: uppercase;
    letter-spacing: .5px;
  }
  .contacts {
    position: absolute;
    left: 40px; top: 244px;
    list-style: none;
    display: flex;
    flex-direction: column;
    gap: 8px;
  }
  .contacts li {
    display: flex;
    align-items: center;
    gap: 10px;
    color: var(--text-light);
    font-size: 19px;
    font-style: italic;
  }
  .contacts svg { width: 16px; height: 16px; flex: none; }

  /* Back */
  .card--back .brand { right: 50px; top: 70px; }
  .card--back .brand__name { font-size: 52px; color: var(--logo-grey); text-align: right; }
  .card--back .brand__mark { width: 26px; height: 26px; background: #55585e; }

  .services {
    position: absolute;
    left: 36px; right: 30px; bottom: 30px;
    color: var(--text-light);
    font-size: 18px;
    font-style: italic;
    line-height: 1.5;
  }
  .services .dot { color: var(--accent); font-style: normal; margin: 0 6px; }
</style>
</head>
<body>

<section class="card card--front" aria-label="Card front">
  <div class="brand">
    <span class="brand__mark"></span>
    <span class="brand__name">Tbm Welding<br>&amp; Fabrication</span>
  </div>

  <p class="holder-name">Dale Hutchins</p>
  <div class="divider"></div>

  <ul class="contacts">
    <li>
      <svg viewBox="0 0 16 16" aria-hidden="true"><path fill="#33a6d7" d="M3.6 1.5l2.3 2.4-1.2 1.8c.9 2 2.4 3.6 4.5 4.6l1.8-1.2 2.4 2.3-1.4 2.1C6.6 13.3 2.5 9.3 1.5 3z"/></svg>
      0438517264
    </li>
    <li>
      <svg viewBox="0 0 16 16" aria-hidden="true"><rect x="1" y="3" width="14" height="10" rx="1" fill="#33a6d7"/><path d="M1.5 3.8L8 9l6.5-5.2" stroke="#141415" stroke-width="1.4" fill="none"/></svg>
      dale@tbmweldingandfabrication.com.au
    </li>
    <li>
      <svg viewBox="0 0 16 16" aria-hidden="true"><circle cx="8" cy="8" r="6.5" fill="none" stroke="#33a6d7" stroke-width="1.5"/><ellipse cx="8" cy="8" rx="2.8" ry="6.5" fill="none" stroke="#33a6d7" stroke-width="1.2"/><path d="M1.5 8h13" stroke="#33a6d7" stroke-width="1.2"/></svg>
      www.tbmweldingandfabrication.com.au
    </li>
  </ul>
</section>

<section class="card card--back" aria-label="Card back">
  <div class="brand">
    <span class="brand__mark"></span>
    <span class="brand__name">Tbm Welding<br>&amp; Fabrication</span>
  </div>

  <p class="services">
    Sheds<span class="dot">•</span>Ute trays<span class="dot">•</span>Cattle and sheep yards<span class="dot">•</span>Trailers<span class="dot">•</span>Farm equipment<br>
    Gateways and Entrances<span class="dot">•</span>Breakdowns<span class="dot">•</span>Maintenance<span class="dot">•</span>And lots more!
  </p>
</section>

</body>
</html>
```